Create a professional, eye-catching business card design that reflects the values and services of Brookfern Veterinary Hospital. we provide veterinary services and the business card should be a memorable representation of the clinic and align with its branding and mission. our tag line is "Faithful Friends, Lifelong Devotion"
Use clean, modern typography. Prioritize readability and professionalism. We would like to see designs that use the color blue, as in the logo example. the final design should communicate professionalism and care, with attention to detail.

```html
<!DOCTYPE html>
<html lang="en">
<head>
<meta charset="utf-8">
<title>Brookfern Veterinary Hospital – Business Card</title>
<link rel="stylesheet" href="https://fonts.googleapis.com/css2?family=Poppins:wght@300;400;500;600;700&display=swap">
<style>
  :root {
    --stage: #232323;
    --paper: #ffffff;
    --navy: #1c3160;
    --navy-ink: #1e3569;
    --light-ink: #e8eef8;
  }
  * { box-sizing: border-box; margin: 0; padding: 0; }
  html, body { width: 1200px; height: 780px; overflow: hidden; }
  body {
    background: var(--stage);
    font-family: "Poppins", sans-serif;
    display: flex;
    align-items: center;
    justify-content: center;
    gap: 40px;
  }
  .card {
    width: 540px;
    height: 309px;
    position: relative;
    overflow: hidden;
    box-shadow: 0 18px 40px rgba(0,0,0,0.55);
  }

  /* Front */
  .card--front { background: var(--paper); color: var(--navy-ink); }
  .brand-mark {
    position: absolute;
    left: 28px; top: 40px;
    width: 210px; height: 170px;
    display: flex; flex-direction: column; align-items: center; justify-content: center;
    gap: 12px;
  }
  .brand-mark__dot {
    width: 52px; height: 52px; border-radius: 50%;
    background: var(--navy-ink);
  }
  .brand-mark__name {
    font-weight: 600; font-size: 15px; line-height: 1.3; text-align: center;
  }
  .divider {
    position: absolute; left: 262px; top: 40px;
    width: 1px; height: 160px; background: var(--navy-ink);
  }
  .contact { position: absolute; left: 290px; top: 42px; }
  .contact__name { font-size: 28px; line-height: 1; white-space: nowrap; }
  .contact__name b { font-weight: 700; }
  .contact__name span { font-weight: 300; }
  .contact__role { font-size: 12px; font-weight: 500; margin-top: 6px; }
  .contact__list { list-style: none; margin-top: 18px; }
  .contact__item {
    display: flex; align-items: center; gap: 9px;
    font-size: 12.5px; font-weight: 400; margin-bottom: 6px;
  }
  .contact__icon { width: 13px; height: 13px; fill: var(--navy-ink); flex: none; }
  .address {
    position: absolute; left: 0; right: 0; bottom: 30px;
    text-align: center; font-size: 14px; font-weight: 500; letter-spacing: 0.3px;
  }

  /* Back */
  .card--back {
    background: radial-gradient(ellipse at 50% 40%, #213a72 0%, var(--navy) 70%);
    display: flex; flex-direction: column; align-items: center; justify-content: center;
  }
  .back-mark { display: flex; flex-direction: column; align-items: center; gap: 14px; }
  .back-mark__dot { width: 60px; height: 60px; border-radius: 50%; background: var(--light-ink); }
  .back-mark__name {
    color: var(--light-ink); font-weight: 500; font-size: 20px; line-height: 1.2;
    text-align: center; white-space: nowrap;
  }
  .tagline {
    margin-top: 34px; color: var(--light-ink);
    font-size: 15px; font-weight: 400; letter-spacing: 0.4px;
  }
</style>
</head>
<body>
  <section class="card card--front" aria-label="Business card front">
    <div class="brand-mark">
      <div class="brand-mark__dot"></div>
      <div class="brand-mark__name">Brookfern Veterinary Hospital</div>
    </div>
    <div class="divider"></div>
    <div class="contact">
      <p class="contact__name"><b>Marta</b> <span>Velinova</span></p>
      <p class="contact__role">Founder &amp; CEO</p>
      <ul class="contact__list">
        <li class="contact__item">
          <svg class="contact__icon" viewBox="0 0 24 24" aria-hidden="true"><path d="M6.6 10.8a15.2 15.2 0 0 0 6.6 6.6l2.2-2.2a1 1 0 0 1 1-.25 11.4 11.4 0 0 0 3.6.57 1 1 0 0 1 1 1V20a1 1 0 0 1-1 1A17 17 0 0 1 3 4a1 1 0 0 1 1-1h3.5a1 1 0 0 1 1 1c0 1.25.2 2.450.57 3.57a1 1 0 0 1-.25 1z"/></svg>
          (555) 014-2236
        </li>
        <li class="contact__item">
          <svg class="contact__icon" viewBox="0 0 24 24" aria-hidden="true"><path d="M2 5h20v14H2z M3.5 6.5 12 13l8.5-6.5" fill="none" stroke="currentColor" stroke-width="2"/><path d="M2 5h20v1.5L12 14 2 6.5z"/></svg>
          info@brookfernvet.com
        </li>
        <li class="contact__item">
          <svg class="contact__icon" viewBox="0 0 24 24" aria-hidden="true"><circle cx="12" cy="12" r="9" fill="none" stroke="currentColor" stroke-width="2"/><path d="M3 12h18M12 3c3 3 3 15 0 18M12 3c-3 3-3 15 0 18" fill="none" stroke="currentColor" stroke-width="1.6"/></svg>
          www.brookfernvet.com
        </li>
      </ul>
    </div>
    <p class="address">1480 Larkmoor Ave. Suite 120 Fort Worth, TX 76104</p>
  </section>

  <section class="card card--back" aria-label="Business card back">
    <div class="back-mark">
      <div class="back-mark__dot"></div>
      <div class="back-mark__name">Brookfern Veterinary Hospital</div>
    </div>
    <p class="tagline">"Faithful Friends, Lifelong Devotion"</p>
  </section>
</body>
</html>
```